Digital Signage Slide Design – Celebrations

I am looking for a digital designer for the design of our Celebration slide for our Digital Signage solution. I have attached two basic designs (landscape & portrait) of our current celebration slide. We are wanting a completely new look and feel that delivers an inspiring layout. Your goals is to provide a design that will grab peoples attention through design and content placement. Note: the final production of the slide will have animated transitioning effects. What we require from you is the design (in PSD format) for both a Landscape (1920 x 1080) and Portrait (1080 x 1920) oriented screen and a written description of how you see the animation working.If you prefer, you can use your own mock-up content and images. What we have supplied in the example mock-up, is only example content.Please refer to the following link to view an example of what a final animated slide looks like - https://www.clipvantor.example/watch?v=QmTb83kLw57 If you are unsure of what a Digital Signage is, please refer to the following page on our website - https://www.brightpanelo.example/industry/corporate-culture
Target Market(s)
Internal Communication Channel for Large Organisations
Colors
Designer to choose colors to be used in the design.
Look and feel
Each slider illustrates characteristics of the customer's brand and the style your logo design should communicate.

```html
<!DOCTYPE html>
<html lang="en">
<head>
<meta charset="utf-8">
<title>Celebration Slide – Work Anniversary</title>
<link rel="stylesheet" href="https://fonts.googleapis.com/css2?family=Open+Sans:wght@700;800&display=swap">
<style>
  :root {
    --bg-deep: #050a35;
    --bg-mid: #0a2a6e;
    --bg-glow: #1468a8;
    --text-light: #ffffff;
    --portrait-dark: #2a1a10;
    --portrait-warm: #8a6238;
    --portrait-light: #b8925c;
  }
  html, body {
    margin: 0;
    padding: 0;
    width: 1200px;
    height: 604px;
    overflow: hidden;
    background: var(--bg-deep);
  }
  .slide {
    position: relative;
    width: 1200px;
    height: 604px;
    overflow: hidden;
    background:
      radial-gradient(ellipse 70% 60% at 55% 55%, rgba(20,104,168,0.55), transparent 70%),
      radial-gradient(ellipse 40% 40% at 100% 60%, rgba(20,104,168,0.45), transparent 70%),
      linear-gradient(180deg, var(--bg-deep) 0%, var(--bg-mid) 55%, #0b3c82 100%);
    font-family: "Open Sans", Arial, sans-serif;
    color: var(--text-light);
  }
  .portrait-frame {
    position: absolute;
    left: 0;
    top: 0;
  }
  .celebrant-line {
    position: absolute;
    left: 447px;
    margin: 0;
    font-weight: 800;
    line-height: 1;
    white-space: nowrap;
  }
  .celebrant-name { font-size: 78px; letter-spacing: 0.5px; }
  .name-first { top: 80px; }
  .name-last { top: 176px; }
  .celebration-date { top: 276px; font-size: 44px; font-weight: 700; }
  .celebration-type { font-size: 78px; }
  .type-first { top: 334px; }
  .type-last { top: 430px; }
</style>
</head>
<body>
  <main class="slide">
    <svg class="portrait-frame" width="1200" height="604" viewBox="0 0 1200 604" role="img" aria-label="Portrait photo of the celebrant in a hexagon frame">
      <defs>
        <linearGradient id="portraitTone" x1="0" y1="0" x2="1" y2="1">
          <stop offset="0" stop-color="var(--portrait-warm)"/>
          <stop offset="0.5" stop-color="var(--portrait-dark)"/>
          <stop offset="1" stop-color="var(--portrait-light)"/>
        </linearGradient>
      </defs>
      <polygon points="224,96 397,182 397,396 224,482 50,396 50,182" fill="url(#portraitTone)"/>
    </svg>

    <h1 class="celebrant-line celebrant-name name-first">Corinna</h1>
    <p class="celebrant-line celebrant-name name-last">Maddox</p>
    <p class="celebrant-line celebration-date">10 September</p>
    <p class="celebrant-line celebration-type type-first">Work</p>
    <p class="celebrant-line celebration-type type-last">Anniversary</p>
  </main>
</body>
</html>
```